Zielgruppe
Kaminholz/Brennholz Verkauf - Zielgruppe Männer zwischen 35-65 Jahren, modernes Design
Aufgabenstellung
Das Plakat sollte modern und erschwinglich gestaltet sein. Es dient als Werbeplakat an einer Brücke über einer vielbefahrenden Straße und soll die Kunden zum Kaminholz Kauf anregen. Auffälliges Design. Design auch im vorbeifahren gut zu erkennen.
Maße 6,00m x 0,90m. Logo & Webseite: www.Feuerscheit-Lindqvist.de soll abgebildet sein.

```html
<!DOCTYPE html>
<html lang="de">
<head>
<meta charset="utf-8">
<title>Lindqvist – Brückenbanner</title>
<link href="https://fonts.googleapis.com/css2?family=Bitter:wght@400;700;800&display=swap" rel="stylesheet">
<style>
  :root {
    --page: #ffffff;
    --brand-red: #e30d18;
    --deep-red: #8a0f12;
    --ember: #3a0c0c;
    --ink: #111111;
    --paper: #ffffff;
    --wood-light: #d9b48c;
    --wood-dark: #8a6a52;
  }
  html, body {
    margin: 0;
    width: 1200px;
    height: 849px;
    overflow: hidden;
    background: var(--page);
  }
  .banner {
    position: absolute;
    left: 82px;
    top: 339px;
    width: 1027px;
    height: 160px;
    background: var(--brand-red);
    overflow: hidden;
    box-shadow: 3px 3px 3px rgba(0,0,0,0.35);
    font-family: "Bitter", Georgia, serif;
  }
  .fire-zone {
    position: absolute;
    left: 726px;
    top: 0;
    width: 301px;
    height: 160px;
    background:
      radial-gradient(ellipse 45% 60% at 80% 20%, rgba(255,140,30,0.8), rgba(255,90,20,0) 70%),
      linear-gradient(100deg, var(--brand-red) 0%, #c8141a 35%, var(--deep-red) 75%, var(--ember) 100%);
  }
  .brand-panel {
    position: absolute;
    left: 0; top: 0;
    width: 270px; height: 160px;
  }
  .brand-name {
    position: absolute;
    left: 0; top: 62px;
    width: 252px;
    text-align: center;
    font-weight: 700;
    font-size: 30px;
    line-height: 36px;
    color: var(--ink);
    margin: 0;
  }
  .claim-strip {
    position: absolute;
    left: 364px; top: 8px;
    width: 318px; height: 22px;
  }
  .claim-text {
    position: absolute;
    left: 364px; top: 11px;
    width: 318px;
    text-align: center;
    color: var(--paper);
    font-size: 12.4px;
    line-height: 16px;
    font-weight: 400;
    margin: 0;
  }
  .headline {
    position: absolute;
    left: 294px; top: 50px;
    margin: 0;
    color: var(--paper);
    font-weight: 700;
    font-size: 40px;
    line-height: 32px;
    transform: rotate(-3deg);
    transform-origin: left top;
    text-shadow: 1px 2px 2px rgba(0,0,0,0.3);
    white-space: nowrap;
  }
  .headline span { display: block; }
  .headline .line-two { padding-left: 126px; }
  .web-address {
    position: absolute;
    left: 355px; top: 120px;
    margin: 0;
    color: var(--paper);
    font-size: 22px;
    line-height: 24px;
    font-weight: 400;
    transform: rotate(-3deg);
    transform-origin: left top;
    white-space: nowrap;
  }
  .pointer {
    position: absolute;
    left: 290px; top: 128px;
    width: 60px; height: 24px;
  }
  .firewood {
    position: absolute;
    left: 713px; top: 27px;
    width: 167px; height: 111px;
    border-radius: 30% 40% 20% 35%;
    background: linear-gradient(160deg, var(--wood-light), var(--wood-dark));
  }
  .price-badge {
    position: absolute;
    left: 869px; top: 18px;
    width: 115px; height: 104px;
    background: var(--ink);
    border-radius: 50%;
    border-bottom-left-radius: 18%;
    color: var(--paper);
    text-align: center;
  }
  .price-badge p { margin: 0; }
  .badge-title { font-weight: 700; font-size: 11.5px; line-height: 14px; padding-top: 17px; }
  .badge-lead { font-size: 11px; line-height: 16px; }
  .badge-price { font-weight: 800; font-size: 20px; line-height: 20px; color: var(--brand-red); }
  .badge-price sup { color: var(--paper); font-size: 12px; }
  .footnote {
    position: absolute;
    left: 853px; top: 129px;
    margin: 0;
    color: var(--paper);
    font-size: 6.6px;
    line-height: 8.4px;
  }
</style>
</head>
<body>
  <section class="banner">
    <div class="fire-zone" role="img" aria-label="Lodernde Flammen als Hintergrund"></div>

    <svg class="brand-panel" viewBox="0 0 270 160" aria-hidden="true">
      <path d="M0 0 H236 C276 40 276 120 226 160 H0 Z" fill="var(--paper)"/>
    </svg>
    <p class="brand-name">Lindqvist</p>

    <svg class="claim-strip" viewBox="0 0 318 22" aria-hidden="true">
      <path d="M6 2 L308 0 L314 6 L312 14 L316 20 L150 21 L4 22 L2 14 L0 10 L5 6 Z" fill="var(--ink)"/>
    </svg>
    <p class="claim-text">Prämium-Qualität schnell &amp; günstig geliefert!</p>

    <h1 class="headline"><span>Kaminholz</span><span class="line-two">auf Bestellung!</span></h1>

    <svg class="pointer" viewBox="0 0 60 24" aria-hidden="true">
      <path d="M0 16 L42 12 M30 2 L58 10 L32 22 L40 12 Z" stroke="var(--ink)" stroke-width="3" fill="var(--ink)" stroke-linejoin="round"/>
    </svg>
    <p class="web-address">www.feuerscheit-lindqvist.de</p>

    <div class="firewood" role="img" aria-label="Gestapelte Buchenholzscheite"></div>

    <div class="price-badge">
      <p class="badge-title">Ofenfertiges<br>Kaminholz</p>
      <p class="badge-lead">Jetzt schon ab</p>
      <p class="badge-price">49,00€<sup>*</sup></p>
    </div>

    <p class="footnote">*pro Schütt-Raummeter (SRM) sortenreines<br>Buchen Brennholz in Premium-Qualität!</p>
  </section>
</body>
</html>
```